Redesign of page from emergency manual

Please redesign this PDF to look better. Please don't include any stock photos. It must be legible. Making some words bold is probably a good idea.

Here are some things I like :

https://tarrowbooks.com.au/collections/frontpage/products/the-plk-v2-ebook

https://img-cd.vostramediafiles.com/qa-ejkwPLOTYY_SuCKbZNu411Qwgjv8YssPxEdzXN93hDkSRjLXK8WmfgbmrJW4ZZ3yUPK=w1052-h592-rw

```html
<!DOCTYPE html>
<html lang="en">
<head>
<meta charset="utf-8">
<title>Hypertension, Acute</title>
<link href="https://fonts.googleapis.com/css2?family=Red+Hat+Display:wght@400;500;600;700;800;900&display=swap" rel="stylesheet">
<style>
  :root {
    --teal: #0097a0;
    --teal-light: #0aa7b1;
    --gold: #aba135;
    --gold-light: #c9bd4c;
    --tick: #e8692a;
    --ink: #1b1b1b;
    --cell: #e4e4e4;
    --cell-soft: #f1f1f1;
    --row-shade: #e8e8e8;
    --paper: #ffffff;
    --backdrop: #eef0f1;
  }
  * { box-sizing: border-box; margin: 0; padding: 0; }
  html, body { width: 1200px; height: 1117px; overflow: hidden; background: var(--backdrop); }
  body { font-family: "Red Hat Display", sans-serif; color: var(--ink); position: relative; }

  .sheet-frame { position: absolute; left: 168px; top: 0; width: 864px; height: 1117px; overflow: hidden; }
  .sheet { position: absolute; left: 0; top: 0; width: 1252px; height: 1620px; background: var(--paper); transform: scale(0.6895); transform-origin: 0 0; }
  .abs { position: absolute; }

  .title-band { left: 0; top: 0; width: 1252px; height: 170px; }
  .title { left: 80px; top: 62px; font-size: 78px; font-weight: 900; color: #fff; letter-spacing: 0.5px; line-height: 1; }

  .intro { left: 100px; top: 204px; width: 1035px; text-align: center; font-size: 26px; font-weight: 500; line-height: 29px; }

  .checks { left: 105px; top: 278px; width: 470px; font-size: 23px; line-height: 27px; }
  .checks li { list-style: none; position: relative; padding-left: 42px; }
  .checks li + li { margin-top: 26px; }
  .tick { width: 22px; height: 18px; position: absolute; left: 0; top: 3px; }
  .tick.orange { fill: none; stroke: var(--tick); stroke-width: 4.5; stroke-linecap: round; stroke-linejoin: round; }
  .tick.white { fill: none; stroke: #fff; stroke-width: 4.5; stroke-linecap: round; stroke-linejoin: round; }

  .caution-bar { left: 84px; top: 460px; width: 471px; height: 54px; background: var(--gold); border-radius: 7px; color: #fff; font-size: 30px; font-weight: 800; text-align: center; line-height: 54px; }
  .caution-text { left: 84px; top: 533px; width: 500px; font-size: 23px; line-height: 26.6px; }

  .range-box { left: 613px; top: 290px; width: 557px; height: 403px; border: 4px solid var(--gold); border-radius: 22px; }
  .range-heading { left: 640px; top: 312px; width: 510px; font-size: 24px; font-weight: 800; line-height: 28px; }
  .range-title { left: 640px; top: 390px; width: 503px; height: 48px; background: var(--teal); border-radius: 4px; color: #fff; font-size: 24px; font-weight: 800; text-align: center; line-height: 46px; }
  .range-table { left: 640px; top: 447px; width: 503px; display: grid; grid-template-columns: 150px 170px 171px; column-gap: 6px; row-gap: 8px; }
  .range-table div { height: 48px; border-radius: 5px; background: var(--cell); display: flex; align-items: center; justify-content: center; font-size: 24px; }
  .range-table .head { background: var(--cell-soft); font-weight: 700; }
  .range-table .soft { background: var(--cell-soft); }

  .drug-head { top: 754px; height: 55px; background: var(--teal); border-radius: 8px; color: #fff; font-size: 25px; font-weight: 800; text-align: center; line-height: 55px; }
  .drug-head.action { left: 84px; width: 291px; }
  .drug-head.drug { left: 382px; width: 786px; }

  .shade { background: var(--row-shade); border-radius: 12px; }
  .action-cell { left: 118px; font-size: 24px; line-height: 27px; font-weight: 500; }
  .drug-list { left: 452px; width: 700px; font-size: 24px; line-height: 27px; font-weight: 500; }
  .drug-list li { list-style: none; position: relative; padding-left: 38px; }
  .drug-list li + li { margin-top: 12px; }

  .diff-band { left: 0; top: 1285px; width: 1225px; height: 76px; }
  .diff-title { left: 0; top: 1285px; width: 1220px; height: 76px; color: #fff; font-size: 37px; font-weight: 800; text-align: center; line-height: 74px; }
  .diff-panel { left: 0; top: 1372px; width: 1220px; height: 217px; background: var(--teal); }
  .diff-list { font-size: 24px; line-height: 31.2px; color: #fff; font-weight: 500; }
  .diff-list li { list-style: none; position: relative; padding-left: 32px; }
  .diff-list .tick { left: 0; top: 7px; }
  .diff-list.left { left: 118px; top: 1406px; }
  .diff-list.right { left: 750px; top: 1404px; }
</style>
</head>
<body>
<svg width="0" height="0" style="position:absolute">
  <defs>
    <symbol id="tick" viewBox="0 0 22 18"><path d="M3 9.5 L8.5 15 L19 3"/></symbol>
    <linearGradient id="tealShade" x1="0" y1="0" x2="1" y2="1">
      <stop offset="0" stop-color="#06aab3"/><stop offset="0.35" stop-color="#0097a0"/>
    </linearGradient>
    <radialGradient id="goldGlow" cx="0.78" cy="0.3" r="0.35">
      <stop offset="0" stop-color="#cfc257"/><stop offset="1" stop-color="#aba135"/>
    </radialGradient>
  </defs>
</svg>

<div class="sheet-frame">
<div class="sheet">

  <svg class="abs title-band" viewBox="0 0 1252 170" aria-hidden="true">
    <polygon points="1044,0 1252,0 1252,149 1085,149 1129,98" fill="var(--gold)"/>
    <polygon points="1125,0 1252,0 1252,110 1210,110" fill="#9f9530" opacity="0.55"/>
    <polygon points="0,33 1049,33 1107,98 1049,165 0,165" fill="url(#tealShade)"/>
  </svg>
  <h1 class="abs title">HYPERTENSION, ACUTE</h1>

  <p class="abs intro">In pediatrics, hypertension is almost always treated by addressing likely causes such as light anesthesia or measurement error:</p>

  <ul class="abs checks">
    <li><svg class="tick orange"><use href="#tick"/></svg>Ensure correct BP cuff size: cuff bladder width ~ 40% of limb circumference</li>
    <li><svg class="tick orange"><use href="#tick"/></svg>Ensure arterial line transducer is at level of heart ( Consider placing arterial line if not already present )</li>
  </ul>

  <div class="abs caution-bar">* CAUTION:</div>
  <p class="abs caution-text">Anti-hypertensive drugs are almost never needed for routine pediatric cases. These medications are used almost exclusively for specialized cardiac, neurosurgical, or endocrine (pheochromocytoma) cases. Consult an expert before use. Rule-out increased ICP.</p>

  <div class="abs range-box"></div>
  <h2 class="abs range-heading">Sustained high blood pressure refractory to treating reversible causes</h2>
  <div class="abs range-title">Hypertensive Blood Pressure Range*</div>
  <div class="abs range-table">
    <div class="head">Age (yr)</div><div class="head">Systolic</div><div class="head">Diastolic</div>
    <div>newborn</div><div>&gt;97</div><div>&gt;70</div>
    <div class="soft">1-3</div><div class="soft">&gt;105</div><div class="soft">&gt;61</div>
    <div>4-12</div><div>&gt;113</div><div>&gt;86</div>
  </div>

  <div class="abs drug-head action">Action</div>
  <div class="abs drug-head drug">Drug (IV Dosing)</div>

  <p class="abs action-cell" style="top:838px">Direct smooth<br>muscle relaxation</p>
  <ul class="abs drug-list" style="top:825px">
    <li><svg class="tick orange"><use href="#tick"/></svg><strong>Sodium nitroprusside</strong> 0.5-10 MICROgrams/kg/min</li>
    <li><svg class="tick orange"><use href="#tick"/></svg><strong>HydrALAZINE</strong> 0.1-0.2 mg/kg (adult dose 5-10 mg)</li>
  </ul>

  <div class="abs shade" style="left:84px;top:920px;width:291px;height:145px"></div>
  <div class="abs shade" style="left:382px;top:920px;width:786px;height:145px"></div>
  <p class="abs action-cell" style="top:966px">Adrenergic<br>blockade</p>
  <ul class="abs drug-list" style="top:931px">
    <li><svg class="tick orange"><use href="#tick"/></svg><strong>Esmolol</strong> 100-500 MICROgrams/kg over 5 min, then 25-300 MICROgrams/kg/min</li>
    <li><svg class="tick orange"><use href="#tick"/></svg><strong>Labetalol</strong> (also α effect) 0.2-1 mg/kg q 10 min; 0.4-3 mg/kg/hour (infusion)</li>
  </ul>

  <p class="abs action-cell" style="top:1091px">Calcium channel<br>blockade</p>
  <ul class="abs drug-list" style="top:1082px">
    <li><svg class="tick orange"><use href="#tick"/></svg><strong>niCARdapine</strong> 0.5-5 MICROgrams/kg/min</li>
    <li><svg class="tick orange"><use href="#tick"/></svg><strong>Clevidipine</strong> 0.5-3.5 MICROgrams/kg/min</li>
  </ul>

  <div class="abs shade" style="left:84px;top:1170px;width:291px;height:53px"></div>
  <div class="abs shade" style="left:382px;top:1170px;width:786px;height:53px"></div>
  <p class="abs action-cell" style="top:1182px">D1-dopamine agonist</p>
  <ul class="abs drug-list" style="top:1182px">
    <li><svg class="tick orange"><use href="#tick"/></svg><strong>Fenoldopam</strong> 0.2-0.8 MICROgrams/kg/min</li>
  </ul>

  <svg class="abs diff-band" viewBox="0 0 1225 76" aria-hidden="true">
    <polygon points="0,0 1190,0 1220,38 1190,76 0,76" fill="url(#goldGlow)"/>
  </svg>
  <h2 class="abs diff-title">Consider Differential (Partial):</h2>
  <div class="abs diff-panel"></div>
  <ul class="abs diff-list left">
    <li><svg class="tick white"><use href="#tick"/></svg>Light anesthesia (consider vaporizer or infusion</li>
    <li><svg class="tick white"><use href="#tick"/></svg>pump empty or malfunctioning)</li>
    <li><svg class="tick white"><use href="#tick"/></svg>Hypercarbia</li>
    <li><svg class="tick white"><use href="#tick"/></svg>Hypoxemia</li>
    <li><svg class="tick white"><use href="#tick"/></svg>Arterial line transducer too low or BP cuff</li>
  </ul>
  <ul class="abs diff-list right">
    <li><svg class="tick white"><use href="#tick"/></svg>too small</li>
    <li><svg class="tick white"><use href="#tick"/></svg>Withdrawal (EtOH or opioid)</li>
    <li><svg class="tick white"><use href="#tick"/></svg>Thyroid Storm</li>
    <li><svg class="tick white"><use href="#tick"/></svg>Pheochromocytoma</li>
    <li><svg class="tick white"><use href="#tick"/></svg>Drug Error</li>
  </ul>

</div>
</div>
</body>
</html>
```